New Company Newsletter Template Needed!!!

We need some new graphics/design for us to create our company newsletter in MS Publisher/Word. Prefer simple, modern design that can be easy to update each month, flexible for adding images and include our company logo (attached).
Also attached our basic existing template but we do not want to use the same “swoosh” ribbon and want to reduce the number of colours used.
Needs to be elements we can move into the software and create a PDF newsletter to circulate.

Font styles to use
Sans Serif

Requirements
Must have
• Company logo
Nice to have
• If any colours should fit into our company logo palette

```html
<!DOCTYPE html>
<html lang="en">
<head>
<meta charset="UTF-8">
<title>Company Newsletter</title>
<link href="https://fonts.googleapis.com/css2?family=Lato:wght@400;700;900&family=Montserrat:wght@700;800;900&display=swap" rel="stylesheet">
<style>
  :root {
    --red: #d0202e;
    --blue: #2b3c8c;
    --navy: #283b7d;
    --ink: #333333;
    --frame: #000000;
    --white: #ffffff;
  }
  * { margin: 0; padding: 0; box-sizing: border-box; }
  html, body { width: 864px; height: 1200px; overflow: hidden; background: var(--frame); }
  .canvas { position: relative; width: 864px; height: 1200px; background: var(--frame); }
  .page {
    position: absolute; left: 13px; top: 18px; width: 833px; height: 1169px;
    background: var(--white); font-family: 'Lato', sans-serif; color: var(--ink); overflow: hidden;
  }
  .masthead { position: absolute; left: 0; top: 0; width: 833px; height: 90px; }
  .masthead svg { position: absolute; left: 0; top: 0; }
  .brand { position: absolute; left: 30px; top: 21px; display: flex; align-items: center; gap: 10px; }
  .brand-mark { width: 48px; height: 48px; border-radius: 50%; background: var(--red); }
  .brand-name { font-family: 'Lato', sans-serif; font-weight: 700; font-size: 40px; color: var(--blue); letter-spacing: -1px; line-height: 1; }
  .issue-tag { position: absolute; right: 12px; top: 13px; color: var(--white); font-weight: 700; font-size: 14px; letter-spacing: .2px; }
  .newsletter-title { position: absolute; right: 12px; top: 46px; font-family: 'Montserrat', sans-serif; font-weight: 900; font-size: 33.5px; color: var(--white); line-height: 1; letter-spacing: .2px; }
  .photo-slot {
    position: absolute; display: flex; flex-direction: column; align-items: center; justify-content: center;
    background: radial-gradient(ellipse at center, #ffffff 0%, #e6e6e6 45%, #bdbdbd 100%);
    color: #8a8a8a; font-family: 'Montserrat', sans-serif; font-weight: 700; text-align: center; line-height: 1;
  }
  .hero-photo { left: 0; top: 90px; width: 833px; height: 368px; font-size: 9.5px; letter-spacing: .5px; }
  .story-photo { left: 397px; top: 874px; width: 376px; height: 234px; font-size: 5px; }
  .contents-title { position: absolute; left: 59px; top: 479px; font-weight: 700; font-size: 25px; color: var(--blue); }
  .contents-box { position: absolute; left: 61px; top: 510px; width: 296px; height: 276px; border: 1.5px solid var(--blue); padding: 14px 10px 0 14px; }
  .contents-box ul { list-style: none; }
  .contents-box li { display: flex; align-items: baseline; height: 41px; font-size: 18.8px; color: var(--blue); }
  .contents-box li::before { content: ""; width: 6px; height: 6px; border-radius: 50%; background: var(--blue); margin-right: 11px; transform: translateY(-4px); }
  .contents-box .leader { flex: 1; overflow: hidden; white-space: nowrap; }
  .contents-box .page-no { color: var(--red); width: 24px; text-align: right; }
  .side-story { position: absolute; left: 61px; top: 817px; width: 302px; }
  .side-story h3 { font-weight: 700; font-size: 19.5px; line-height: 24.5px; color: var(--red); margin-bottom: 6px; }
  .body-copy { font-size: 18.4px; line-height: 25.9px; text-align: justify; hyphens: auto; }
  .lead-story { position: absolute; left: 397px; top: 476px; width: 376px; }
  .lead-story h1 { font-family: 'Montserrat', sans-serif; font-weight: 700; font-size: 31px; color: var(--red); line-height: 1.2; margin-bottom: 4px; letter-spacing: -.3px; }
  .footer-band { position: absolute; left: 0; bottom: 0; width: 833px; height: 43px; background: var(--navy); color: var(--white); font-weight: 700; font-size: 14px; display: flex; justify-content: space-between; align-items: center; padding: 0 13px 0 15px; }
</style>
</head>
<body>
<div class="canvas">
  <div class="page">
    <header class="masthead">
      <svg width="833" height="90" viewBox="0 0 833 90">
        <polygon points="352,0 833,0 833,90 304,90" fill="var(--red)"/>
        <polygon points="344,0 352,0 304,90 296,90" fill="var(--blue)"/>
        <polygon points="543,10 833,10 833,37 566,37" fill="var(--blue)"/>
      </svg>
      <div class="brand">
        <span class="brand-mark"></span>
        <span class="brand-name">Brightway</span>
      </div>
      <span class="issue-tag">DATE (MONTH YEAR)&nbsp; VOL. #, ISSUE #</span>
      <span class="newsletter-title">NEWSLETTER TITLE HERE</span>
    </header>

    <div class="photo-slot hero-photo" role="img" aria-label="Cover photo placeholder">
      <svg width="70" height="46" viewBox="0 0 70 46"><rect x="1" y="1" width="68" height="44" fill="none" stroke="#8a8a8a" stroke-width="1.5"/><circle cx="17" cy="11" r="5" fill="none" stroke="#8a8a8a" stroke-width="1.5"/><polyline points="1,32 20,24 30,30 48,15 69,36" fill="none" stroke="#8a8a8a" stroke-width="1.5"/></svg>
      <div style="margin-top:3px">PLACE YOUR<br>PHOTO</div>
    </div>

    <h2 class="contents-title">Inside this Issue</h2>
    <nav class="contents-box">
      <ul>
        <li><span class="leader">Inside Story Title....................................</span><span class="page-no">2</span></li>
        <li><span class="leader">Inside Story Title....................................</span><span class="page-no">2</span></li>
        <li><span class="leader">Inside Story Title....................................</span><span class="page-no">3</span></li>
        <li><span class="leader">Inside Story Title....................................</span><span class="page-no">3</span></li>
        <li><span class="leader">Inside Story Title....................................</span><span class="page-no">4</span></li>
        <li><span class="leader">Inside Story Title....................................</span><span class="page-no">4</span></li>
      </ul>
    </nav>

    <article class="side-story">
      <h3>Parraphgh title text&nbsp; Parraphgh title text&nbsp; Parraphgh title text</h3>
      <p class="body-copy">This story can fit 125-165 words. This is greeked text for copy placement. Use this as a placeholder for text when it's not readily available.&nbsp; This is a layout tool intended to aid in the design process, to provide adequate amounts of copy to proof a layout and style. It's a necessary element for building good design.</p>
    </article>

    <article class="lead-story">
      <h1>Lead Story Headline</h1>
      <p class="body-copy">This story can fit 125-165 words. This is greeked text for copy placement. Use this as a placeholder for text when it's not readily avail&shy;able.&nbsp; This is a layout tool intended to aid in the design process, to provide adequate amounts of copy to proof a layout and style. It's a neces&shy;sary element for building good design. Greeked copy is a standard in the marketing industry. The process of This story can fit 125-165 words. This is greeked text for copy placement. Use this as a placeholder for text when it's not readily available.&nbsp; This is a layout tool intended to aid in the design process</p>
    </article>

    <div class="photo-slot story-photo" role="img" aria-label="Lead story photo placeholder">
      <svg width="30" height="27" viewBox="0 0 30 27"><rect x="1" y="1" width="28" height="25" fill="none" stroke="#8a8a8a" stroke-width="1"/><circle cx="8" cy="7" r="2.5" fill="none" stroke="#8a8a8a" stroke-width="1"/><polyline points="1,19 9,14 13,18 21,9 29,20" fill="none" stroke="#8a8a8a" stroke-width="1"/></svg>
      <div style="margin-top:2px">PLACE YOUR<br>PHOTO</div>
    </div>

    <footer class="footer-band">
      <span>COPYRIHT TEXT HERE</span>
      <span>DATE (MONTH YEAR) | VOL. #, ISSUE #</span>
    </footer>
  </div>
</div>
</body>
</html>
```